Groovy little Insurance brokerage needs a new look

We have a new logo, but need to work out how to make it work for us!
We are a small insurance broking firm (three staff with different focus and styles), with lots of energy, experience and enthusiasm. A focus on both commercial and domestic market. We would like our cards to show a fresh look - while veering away from the 'run of the mill' insurance industry (often dull) approach.
Updates

Thanks to all for your concepts.

Had some great ideas come back, now just the process of picking which one is going to work best for us...
Will advise when we've had an opportunity to review.

Thanks!
From the team at
Kestrel Dunmore Insurance Brokers

Thanks SO much to all of your for your great designs.  Now just a process of sorting out the favorites.  If yours is eliminated, just want to say a collective thank you for your efforts!

Industry/Entity Type

Business

```html
<!DOCTYPE html>
<html lang="en">
<head>
<meta charset="utf-8">
<title>Kestrel Dunmore Insurance Brokers – Business Card</title>
<link rel="stylesheet" href="https://fonts.googleapis.com/css2?family=Montserrat:wght@600&family=Russo+One&family=Arimo&display=swap">
<style>
  :root {
    --backdrop: #1c1c1c;
    --card-white: #f4f4f4;
    --card-dark: #2a2a2a;
    --brand-teal: #2ab3d6;
    --name-teal: #2a8d9b;
    --name-white: #ffffff;
    --muted-grey: #7a7a7a;
    --watermark: #343434;
    --icon-grey: #a9a9a9;
  }
  * { box-sizing: border-box; margin: 0; padding: 0; }
  html, body {
    width: 1200px;
    height: 900px;
    overflow: hidden;
    background: var(--backdrop);
  }
  .stage { position: relative; width: 1200px; height: 900px; }
  .card {
    position: absolute;
    left: 320px;
    width: 560px;
    height: 320px;
    border-radius: 3px;
    overflow: hidden;
  }
  .card--front {
    top: 105px;
    background: var(--card-white);
    display: flex;
    align-items: center;
    justify-content: center;
    gap: 16px;
  }
  .brand-dot {
    width: 30px; height: 30px;
    border-radius: 50%;
    background: var(--brand-teal);
    flex: none;
  }
  .brand-name {
    font-family: "Montserrat", sans-serif;
    font-weight: 600;
    font-size: 22px;
    line-height: 1.25;
    letter-spacing: 1px;
    text-transform: uppercase;
    color: var(--brand-teal);
  }
  .card--back { top: 475px; background: var(--card-dark); }
  .owner { position: absolute; top: 28px; left: 270px; }
  .owner-name {
    font-family: "Russo One", sans-serif;
    font-size: 27px;
    font-variant: small-caps;
    letter-spacing: 1.5px;
    color: var(--name-white);
  }
  .owner-name .accent { color: var(--name-teal); }
  .owner-role {
    font-family: "Arimo", sans-serif;
    font-size: 21px;
    color: var(--muted-grey);
    margin-top: -2px;
  }
  .watermark {
    position: absolute;
    top: 98px;
    left: 20px;
    display: flex;
    align-items: center;
    gap: 14px;
    color: var(--watermark);
  }
  .watermark-dot {
    width: 62px; height: 62px;
    border-radius: 50%;
    background: var(--watermark);
    flex: none;
  }
  .watermark-name {
    font-family: "Montserrat", sans-serif;
    font-weight: 600;
    text-transform: uppercase;
    white-space: nowrap;
    line-height: 1.1;
  }
  .watermark-name .line-main { display: block; font-size: 36px; letter-spacing: 1px; }
  .watermark-name .line-sub { display: block; font-size: 17px; letter-spacing: 3px; }
  .contact-list {
    position: absolute;
    left: 24px;
    top: 188px;
    list-style: none;
    display: flex;
    flex-direction: column;
    gap: 10px;
  }
  .contact-item {
    display: flex;
    align-items: center;
    gap: 12px;
    font-family: "Arimo", sans-serif;
    font-size: 14px;
    color: var(--icon-grey);
  }
  .contact-item svg { display: block; width: 22px; height: 20px; flex: none; fill: none; stroke: var(--icon-grey); stroke-width: 1.6; }
  .contact-item .solid { fill: var(--icon-grey); stroke: none; }
</style>
</head>
<body>
<main class="stage">
  <section class="card card--front" aria-label="Card front">
    <span class="brand-dot"></span>
    <span class="brand-name">Kestrel Dunmore<br>Insurance Brokers</span>
  </section>

  <section class="card card--back" aria-label="Card back">
    <div class="owner">
      <p class="owner-name">Owner’s <span class="accent">Name</span></p>
      <p class="owner-role">Designation</p>
    </div>

    <div class="watermark" aria-hidden="true">
      <span class="watermark-dot"></span>
      <span class="watermark-name">
        <span class="line-main">Kestrel Dunmore</span>
        <span class="line-sub">Insurance Brokers</span>
      </span>
    </div>

    <ul class="contact-list">
      <li class="contact-item"><svg viewBox="0 0 22 20" aria-hidden="true"><path class="solid" d="M11 1a5.5 5.5 0 0 0-5.5 5.5C5.5 10.5 11 18 11 18s5.5-7.5 5.5-11.5A5.5 5.5 0 0 0 11 1zm0 8a2.3 2.3 0 1 1 0-4.6A2.3 2.3 0 0 1 11 9z"/></svg><span>12 Harbour Lane, Kestrel Bay</span></li>
      <li class="contact-item"><svg viewBox="0 0 22 20" aria-hidden="true"><path class="solid" d="M2 6c0-2 4-3.5 9-3.5S20 4 20 6v2h-4V6.5c-1.5-.6-8.5-.6-10 0V8H2zM5 9h12l2 8H3zm6 1.8a2.6 2.6 0 1 0 0 5.2 2.6 2.6 0 0 0 0-5.2z"/></svg><span>+00 3 555 0142</span></li>
      <li class="contact-item"><svg viewBox="0 0 22 20" aria-hidden="true"><circle cx="11" cy="10" r="8"/><ellipse cx="11" cy="10" rx="3.5" ry="8"/><path d="M3 10h16M4.5 5.5h13M4.5 14.5h13"/></svg><span>www.kestreldunmore.example</span></li>
      <li class="contact-item"><svg viewBox="0 0 22 20" aria-hidden="true"><rect x="1.5" y="4" width="19" height="13"/><path d="M1.5 4l9.5 7 9.5-7"/></svg><span>hello@kestreldunmore.example</span></li>
    </ul>
  </section>
</main>
</body>
</html>
```